I need a simple infographic that describes the 4 basic elements of how to effectively create change.

The overall title (Gentle Pressure Relentlessly Applied) should be at the top of the infographic. Subtitle is: "Leading Change".
There are four steps:
1. Alignment- Agreement on Approach
2. Transparency- Metrics for Assurance
3. Skills- Training and Coaching
4. Integrity- Culture of Accountability

Target Market(s)

Business Leaders in a training workshop

Font styles to use
Serif

Requirements
Must have
• Here are the 4 elements of the Infographic: Please show them in order.
• 1. Agreement on Approach. (Alignment)
• 2. Metrics for Assurance (Transparency)
• 3. Training and Coaching (Skills)
• 4. Culture of Accountability (Integrity)
Nice to have
• Cool Graphics that depict the 4 steps.
Should not have
• Pictures.

```html
<!DOCTYPE html>
<html lang="en">
<head>
<meta charset="utf-8">
<title>Gentle Pressure Relentlessly Applied – Leading Change</title>
<link rel="stylesheet" href="https://fonts.googleapis.com/css2?family=Barlow+Condensed:wght@400;500;600;700&display=swap">
<style>
  :root {
    --page-bg: #f4f1ec;
    --card-bg: #ececec;
    --navy: #1f3a78;
    --teal: #2a9a72;
    --rule-start: #25a27c;
    --rule-end: #0f6a4f;
    --footer-start: #0d1736;
    --footer-end: #1e3b7c;
    --shadow: rgba(0, 0, 0, 0.18);
    --arrow: #a6a6a6;

    --s1-light: #2fb98d; --s1-dark: #0d7555; --s1-tab: #1b7a5c;
    --s2-light: #6f89c6; --s2-dark: #22387a; --s2-tab: #1f3470;
    --s3-light: #5dbb4b; --s3-dark: #2a8a2d; --s3-tab: #2d8b31;
    --s4-light: #f8ab25; --s4-dark: #e56d12; --s4-tab: #e07010;
  }
  * { margin: 0; padding: 0; box-sizing: border-box; }
  html, body { width: 1200px; height: 1200px; overflow: hidden; }
  body {
    background: var(--page-bg);
    font-family: "Barlow Condensed", "Arial Narrow", sans-serif;
    position: relative;
  }
  .infographic {
    position: absolute;
    left: 50px; top: 230px;
    width: 1100px; height: 740px;
    background: var(--card-bg);
    box-shadow: 0 6px 18px rgba(0,0,0,0.15);
    overflow: hidden;
  }
  .title {
    position: absolute;
    left: 37px; top: 38px;
    color: var(--navy);
    font-weight: 600;
    font-size: 52px;
    line-height: 52px;
    letter-spacing: 0.2px;
    text-transform: uppercase;
  }
  .title-rule {
    position: absolute;
    left: 37px; top: 155px;
    width: 1027px; height: 3px;
    background: linear-gradient(90deg, var(--rule-start), var(--rule-end));
  }
  .subtitle {
    position: absolute;
    left: 37px; top: 176px;
    color: var(--teal);
    font-weight: 600;
    font-size: 50px;
    line-height: 50px;
    text-transform: uppercase;
  }
  .step {
    position: absolute;
    top: 279px;
    width: 200px;
  }
  .step-1 { left: 43px;  --light: var(--s1-light); --dark: var(--s1-dark); --tab: var(--s1-tab); }
  .step-2 { left: 311px; --light: var(--s2-light); --dark: var(--s2-dark); --tab: var(--s2-tab); }
  .step-3 { left: 579px; --light: var(--s3-light); --dark: var(--s3-dark); --tab: var(--s3-tab); }
  .step-4 { left: 847px; --light: var(--s4-light); --dark: var(--s4-dark); --tab: var(--s4-tab); }

  .step-tab {
    display: block;
    width: 104px; height: 27px;
    background: var(--tab);
    color: #fff;
    font-weight: 700;
    font-size: 21px;
    line-height: 27px;
    padding-left: 15px;
    clip-path: polygon(0 0, 88% 0, 100% 50%, 88% 100%, 0 100%);
  }
  .step-card {
    position: relative;
    width: 200px;
    box-shadow: 9px 9px 0 var(--shadow);
  }
  .step-head {
    height: 89px;
    background: linear-gradient(90deg, var(--light), var(--dark));
    color: #fff;
    text-align: center;
    padding-top: 11px;
  }
  .step-name {
    font-weight: 600;
    font-size: 29px;
    line-height: 28px;
    letter-spacing: 0.5px;
    text-transform: uppercase;
  }
  .step-desc {
    font-weight: 500;
    font-size: 18px;
    line-height: 21px;
    text-transform: uppercase;
    margin-top: 3px;
  }
  .step-body {
    height: 167px;
    background: #fff;
    display: flex;
    align-items: center;
    justify-content: center;
  }
  .step-icon {
    width: 130px; height: 120px;
    border-radius: 8px;
    background: linear-gradient(135deg, var(--light), var(--dark));
    opacity: 0.28;
  }
  .connector {
    position: absolute;
    top: 428px;
    width: 56px; height: 44px;
  }
  .connector-1 { left: 252px; }
  .connector-2 { left: 520px; }
  .connector-3 { left: 788px; }

  .footer {
    position: absolute;
    left: 0; bottom: 0;
    width: 1100px; height: 65px;
    background: linear-gradient(90deg, var(--footer-start), var(--footer-end));
  }
  .brand {
    position: absolute;
    right: 48px; top: 13px;
    display: flex;
    align-items: center;
    gap: 10px;
    color: #fff;
    font-weight: 500;
    font-size: 30px;
    line-height: 40px;
    letter-spacing: 0.5px;
  }
  .brand-dot {
    width: 38px; height: 38px;
    border-radius: 50%;
    border: 2px solid #fff;
  }
</style>
</head>
<body>
  <main class="infographic">
    <h1 class="title">Gentle Pressure<br>Relentlessly Applied</h1>
    <div class="title-rule"></div>
    <h2 class="subtitle">Leading Change</h2>

    <section class="step step-1">
      <span class="step-tab">STEP 1</span>
      <div class="step-card">
        <div class="step-head">
          <div class="step-name">Alignment</div>
          <div class="step-desc">Agreement on<br>Approach</div>
        </div>
        <div class="step-body">
          <div class="step-icon" role="img" aria-label="Icon: signed agreement document beside a stack of papers"></div>
        </div>
      </div>
    </section>

    <svg class="connector connector-1" viewBox="0 0 56 44" aria-hidden="true"><polygon points="0,0 40,0 56,22 40,44 0,44" fill="var(--arrow)"/></svg>

    <section class="step step-2">
      <span class="step-tab">STEP 2</span>
      <div class="step-card">
        <div class="step-head">
          <div class="step-name">Transparency</div>
          <div class="step-desc">Metrics for<br>Assurance</div>
        </div>
        <div class="step-body">
          <div class="step-icon" role="img" aria-label="Icon: laptop showing a rising line chart with a check mark"></div>
        </div>
      </div>
    </section>

    <svg class="connector connector-2" viewBox="0 0 56 44" aria-hidden="true"><polygon points="0,0 40,0 56,22 40,44 0,44" fill="var(--arrow)"/></svg>

    <section class="step step-3">
      <span class="step-tab">STEP 3</span>
      <div class="step-card">
        <div class="step-head">
          <div class="step-name">Skills</div>
          <div class="step-desc">Training and<br>Coaching</div>
        </div>
        <div class="step-body">
          <div class="step-icon" role="img" aria-label="Icon: trainer pointing at a presentation board"></div>
        </div>
      </div>
    </section>

    <svg class="connector connector-3" viewBox="0 0 56 44" aria-hidden="true"><polygon points="0,0 40,0 56,22 40,44 0,44" fill="var(--arrow)"/></svg>

    <section class="step step-4">
      <span class="step-tab">STEP 4</span>
      <div class="step-card">
        <div class="step-head">
          <div class="step-name">Integrity</div>
          <div class="step-desc">Culture of<br>Accountability</div>
        </div>
        <div class="step-body">
          <div class="step-icon" role="img" aria-label="Icon: two team members with a check mark badge"></div>
        </div>
      </div>
    </section>

    <footer class="footer">
      <div class="brand"><span class="brand-dot"></span><span>THE HARLOW GROUP</span></div>
    </footer>
  </main>
</body>
</html>
```